Business Card design for a company called Tallow Flame NI

I need a business card design for my oil fired boiler servicing company. I have a logo design already and Im just looking that incorporated into the business card design. card details; Tallow Flame NI
Oil Burner Servicing - Mid Ulster Area
Service Engineer - Owen Marsh
Mobile 07751364927
email - Tallow.Flame.NI@hearthmail.example
www.tallowflameni.example
I carry out Servicing, Commissioning, Fault Finding, Warranty Validation
Target Market(s)
home owners with oil fired central heating
Industry/Entity Type
Business
Contact Information for Business Card
Tallow Flame NI
Tell. 07751364927
Web: www.tallowflameni.example
email Tallow.Flame.NI@Hearthmail.Example
Servicing Fault Finding Commissioning Warranty Validation
Look and feel

```html
<!DOCTYPE html>
<html lang="en">
<head>
<meta charset="utf-8">
<title>Tallow Flame NI – Business Card</title>
<link rel="stylesheet" href="https://fonts.googleapis.com/css2?family=Didact+Gothic&display=swap">
<style>
  :root {
    --backdrop: #d8d8d6;
    --card-light: #f3f3f1;
    --card-dark: #2d2d2d;
    --brand-green: #6dbe45;
    --ink-grey: #555555;
    --ink-soft: #8a8a8a;
    --ink-light: #d6d6d6;
  }
  * { margin: 0; padding: 0; box-sizing: border-box; }
  html, body {
    width: 1200px;
    height: 747px;
    overflow: hidden;
    background: var(--backdrop);
    font-family: "Didact Gothic", "Century Gothic", sans-serif;
  }
  .stage {
    position: relative;
    width: 1200px;
    height: 747px;
  }
  .card {
    position: absolute;
    top: 219px;
    width: 540px;
    height: 309px;
    box-shadow: 0 6px 18px rgba(0,0,0,0.18);
  }
  .card--front { left: 40px; background: var(--card-light); }
  .card--back  { left: 620px; background: var(--card-dark); }

  /* brand lockup */
  .brand { position: absolute; display: flex; align-items: center; gap: 8px; }
  .brand__dot {
    width: 30px; height: 30px; border-radius: 50%;
    background: var(--brand-green); flex: none;
  }
  .brand__name {
    color: var(--brand-green);
    font-size: 25px;
    line-height: 1;
    letter-spacing: 0.2px;
  }
  .brand__tagline {
    display: block;
    font-size: 6.5px;
    letter-spacing: 0.4px;
    text-transform: uppercase;
    margin-top: 3px;
  }
  .card--front .brand { left: 26px; top: 112px; }
  .card--front .brand__tagline { color: var(--ink-soft); }
  .card--back .brand { left: 262px; top: 128px; }
  .card--back .brand__dot { width: 40px; height: 40px; }
  .card--back .brand__name { font-size: 30px; }
  .card--back .brand__tagline { color: var(--ink-light); font-size: 7.5px; }

  /* contact block */
  .contact { position: absolute; left: 252px; top: 150px; }
  .contact__name {
    font-size: 26px; color: var(--ink-grey); line-height: 1.05;
  }
  .contact__role {
    font-size: 12px; color: var(--brand-green); margin-bottom: 10px;
  }
  .contact__list { list-style: none; }
  .contact__item {
    display: flex; align-items: center; gap: 8px;
    font-size: 12.5px; color: var(--ink-grey);
    margin-bottom: 6px; white-space: nowrap;
  }
  .contact__icon { width: 11px; height: 11px; flex: none; }

  /* services list */
  .services {
    position: absolute; left: 32px; top: 112px; list-style: none;
  }
  .services__item {
    display: flex; align-items: center; gap: 10px;
    font-size: 17px; color: var(--ink-light);
    margin-bottom: 8px;
  }
  .services__tick { width: 14px; height: 14px; flex: none; }
</style>
</head>
<body>
<main class="stage">

  <section class="card card--front" aria-label="Business card front">
    <div class="brand">
      <span class="brand__dot"></span>
      <div>
        <span class="brand__name">Tallow Flame NI</span>
        <span class="brand__tagline">Oil Burner Servicing - Mid Ulster Area</span>
      </div>
    </div>

    <div class="contact">
      <p class="contact__name">Owen Marsh</p>
      <p class="contact__role">Service Engineer</p>
      <ul class="contact__list">
        <li class="contact__item">
          <svg class="contact__icon" viewBox="0 0 12 12" aria-hidden="true">
            <rect width="12" height="12" rx="1.5" fill="var(--brand-green)"/>
            <path d="M3 4.2c0-.8 2.2-1.3 3-1.3s3 .5 3 1.3v.8H7.5v-.6h-3v.6H3z M3.6 6h4.8l.6 3.2H3z" fill="#fff"/>
          </svg>
          <span>07751364927</span>
        </li>
        <li class="contact__item">
          <svg class="contact__icon" viewBox="0 0 12 12" aria-hidden="true">
            <circle cx="6" cy="6" r="5.5" fill="var(--ink-soft)"/>
            <path d="M.8 6h10.4M6 .6v10.8M2 3h8M2 9h8" stroke="#fff" stroke-width=".7" fill="none"/>
            <ellipse cx="6" cy="6" rx="2.4" ry="5.3" stroke="#fff" stroke-width=".7" fill="none"/>
          </svg>
          <span>www.tallowflameni.example</span>
        </li>
        <li class="contact__item">
          <svg class="contact__icon" viewBox="0 0 12 12" aria-hidden="true">
            <rect y="1.5" width="12" height="9" fill="var(--brand-green)"/>
            <path d="M.5 2l5.5 4.5L11.5 2M.5 10l4-4M11.5 10l-4-4" stroke="#fff" stroke-width=".8" fill="none"/>
          </svg>
          <span>Tallow.Flame.NI@Hearthmail.Example</span>
        </li>
      </ul>
    </div>
  </section>

  <section class="card card--back" aria-label="Business card back">
    <ul class="services">
      <li class="services__item">
        <svg class="services__tick" viewBox="0 0 14 14" aria-hidden="true">
          <rect x=".75" y="1.75" width="11.5" height="11.5" fill="none" stroke="var(--brand-green)" stroke-width="1.2"/>
          <path d="M3 7l3 3.5L13 1" stroke="var(--brand-green)" stroke-width="1.8" fill="none"/>
        </svg>
        <span>Servicing</span>
      </li>
      <li class="services__item">
        <svg class="services__tick" viewBox="0 0 14 14" aria-hidden="true">
          <rect x=".75" y="1.75" width="11.5" height="11.5" fill="none" stroke="var(--brand-green)" stroke-width="1.2"/>
          <path d="M3 7l3 3.5L13 1" stroke="var(--brand-green)" stroke-width="1.8" fill="none"/>
        </svg>
        <span>Commissioning</span>
      </li>
      <li class="services__item">
        <svg class="services__tick" viewBox="0 0 14 14" aria-hidden="true">
          <rect x=".75" y="1.75" width="11.5" height="11.5" fill="none" stroke="var(--brand-green)" stroke-width="1.2"/>
          <path d="M3 7l3 3.5L13 1" stroke="var(--brand-green)" stroke-width="1.8" fill="none"/>
        </svg>
        <span>Fault Finding</span>
      </li>
      <li class="services__item">
        <svg class="services__tick" viewBox="0 0 14 14" aria-hidden="true">
          <rect x=".75" y="1.75" width="11.5" height="11.5" fill="none" stroke="var(--brand-green)" stroke-width="1.2"/>
          <path d="M3 7l3 3.5L13 1" stroke="var(--brand-green)" stroke-width="1.8" fill="none"/>
        </svg>
        <span>Warranty Validation</span>
      </li>
    </ul>

    <div class="brand">
      <span class="brand__dot"></span>
      <div>
        <span class="brand__name">Tallow Flame NI</span>
        <span class="brand__tagline">Oil Burner Servicing - Mid Ulster Area</span>
      </div>
    </div>
  </section>

</main>
</body>
</html>
```